Local Roofing/Construction company business needs new biz card design

We need a new business card design, current cards are from the start of this operation and generic at best. We are a local Construction Company (General Contractor) with a majority of our work originating from insurance claims-exterior finish work is the main focus (Roofs-Siding-Gutters etc). Heavily involved with homeowners and the low ball offers they receive from insurance company's after a insurable event takes place. I have attached some of our original logo file(s) below.

```html
<!DOCTYPE html>
<html lang="de">
<head>
<meta charset="utf-8">
<title>Nordwall Construction – Visitenkarte</title>
<link rel="stylesheet" href="https://fonts.googleapis.com/css2?family=Cherry+Swash:wght@700&family=Jost:wght@300;400;700&display=swap">
<style>
  :root {
    --green: #5bbd72;
    --cream: #f8f6f3;
    --ink: #0e1f22;
    --white: #ffffff;
    --backdrop: #eef0f1;
  }
  * { box-sizing: border-box; margin: 0; padding: 0; }
  html, body { width: 1199px; height: 1200px; overflow: hidden; }
  body { background: var(--backdrop); position: relative; font-family: "Jost", sans-serif; }

  .card { position: absolute; left: 169px; width: 860px; height: 504px; overflow: hidden; }
  .card--front { top: 77px; background: var(--cream); }
  .card--back { top: 618px; background: var(--green); }

  .card__shape { position: absolute; inset: 0; width: 860px; height: 504px; }

  .brand-block {
    position: absolute; left: 40px; top: 0; width: 380px; height: 504px;
    display: flex; align-items: center; justify-content: center; gap: 14px;
  }
  .brand-block__square { width: 22px; height: 22px; background: var(--green); flex: none; }
  .brand-name {
    font-family: "Jost", sans-serif; font-weight: 700; color: var(--green);
    font-size: 38px; line-height: 1.05; letter-spacing: 1px; text-transform: uppercase;
  }

  .contact { position: absolute; right: 58px; top: 0; width: 380px; text-align: right; color: var(--white); }
  .contact__name {
    position: absolute; right: 0; top: 100px;
    font-family: "Cherry Swash", serif; font-weight: 700; font-size: 36px; color: var(--ink);
    white-space: nowrap;
  }
  .contact__role { position: absolute; right: 0; top: 155px; font-weight: 300; font-size: 19px; }
  .contact__list { list-style: none; }
  .contact__item {
    position: absolute; right: 0; display: flex; align-items: center; gap: 12px;
    font-weight: 300; font-size: 19px; white-space: nowrap; line-height: 1.5;
  }
  .contact__item svg { width: 14px; height: 14px; flex: none; fill: var(--ink); }
  .contact__item--phone { top: 221px; }
  .contact__item--mail { top: 259px; }
  .contact__item--web { top: 296px; }
  .contact__item--address { top: 346px; align-items: flex-start; }
  .contact__item--address svg { margin-top: 8px; }
  .contact__item--address span { display: block; text-align: center; line-height: 1.5; }

  .back-brand {
    position: absolute; left: 135px; top: 175px; width: 592px; height: 152px;
    display: flex; align-items: center; justify-content: center; gap: 20px;
  }
  .back-brand__square { width: 26px; height: 26px; background: var(--white); flex: none; }
  .back-brand__name {
    font-family: "Jost", sans-serif; font-weight: 700; color: var(--white);
    font-size: 46px; line-height: 1.0; letter-spacing: 1px; text-transform: uppercase;
  }
</style>
</head>
<body>

<section class="card card--front" aria-label="Visitenkarte Vorderseite">
  <svg class="card__shape" viewBox="0 0 860 504" aria-hidden="true">
    <polygon points="491,0 860,0 860,504 491,504 441,454 441,50" fill="var(--green)"/>
  </svg>

  <div class="brand-block">
    <span class="brand-block__square"></span>
    <p class="brand-name">Nordwall<br>Construction</p>
  </div>

  <div class="contact">
    <h1 class="contact__name">Tomas Berghoff</h1>
    <p class="contact__role">Geschäftsführer</p>
    <ul class="contact__list">
      <li class="contact__item contact__item--phone">+49 1520 482 1937
        <svg viewBox="0 0 24 24"><path d="M6.6 10.8a15.1 15.1 0 0 0 6.6 6.6l2.2-2.2c.3-.3.7-.4 1-.2 1.1.4 2.3.6 3.6.6.6 0 1 .4 1 1V20c0 .6-.4 1-1 1A17 17 0 0 1 3 4c0-.6.4-1 1-1h3.5c.6 0 1 .4 1 1 0 1.3.2 2.5.6 3.6.1.3 0 .7-.2 1z"/></svg>
      </li>
      <li class="contact__item contact__item--mail">tomas@nordwallbau.com
        <svg viewBox="0 0 24 24"><path d="M2 5h20v14H2z M2 5l10 8 10-8" fill="var(--ink)" stroke="var(--green)" stroke-width="1.5"/></svg>
      </li>
      <li class="contact__item contact__item--web">www.nordwallbau.com
        <svg viewBox="0 0 24 24"><circle cx="12" cy="12" r="10"/><path d="M2 12h20M12 2c3 3 3 17 0 20M12 2c-3 3-3 17 0 20" stroke="var(--green)" stroke-width="1.4" fill="none"/></svg>
      </li>
      <li class="contact__item contact__item--address"><span>Lindenweg 14<br>91177 Hollerbach</span>
        <svg viewBox="0 0 24 24"><path d="M12 1a7 7 0 0 0-7 7c0 5 7 12 7 12s7-7 7-12a7 7 0 0 0-7-7zm0 9.5A2.5 2.5 0 1 1 12 5.5a2.5 2.5 0 0 1 0 5z"/><rect x="6" y="21" width="12" height="2"/></svg>
      </li>
    </ul>
  </div>
</section>

<section class="card card--back" aria-label="Visitenkarte Rückseite">
  <svg class="card__shape" viewBox="0 0 860 504" aria-hidden="true">
    <polygon points="110,112 752,112 787,147 787,352 752,387 110,387 75,352 75,147"
             fill="none" stroke="var(--white)" stroke-width="5"/>
    <polygon points="153,175 709,175 727,193 727,309 709,327 153,327 135,309 135,193"
             fill="var(--ink)"/>
  </svg>
  <div class="back-brand">
    <span class="back-brand__square"></span>
    <p class="back-brand__name">Nordwall<br>Construction</p>
  </div>
</section>

</body>
</html>
```